LRW Automotive needs a catchy banner design

We need a design for a banner to be displayed on the fence in the outfield of a baseball stadium to show off our company and have people interested in what we do. We need something catchy that's going to attract people to look over at our banner.
We are a
Total Vehicle Care Company
Tires - Service - Repair - Diesel
We are in a Town called Maple Ridge
(555)214-3086 we would like the phone number to be a descent size so when you are in the stands you can read it.
I have attached what we came up with but like I said we need it to pop more and make the viewer that's looking at it want to look us up.
The Banner size is 24ft long and 10ft tall

```html
<!DOCTYPE html>
<html lang="en">
<head>
<meta charset="utf-8">
<title>LRW Automotive – Outfield Banner</title>
<link rel="stylesheet" href="https://fonts.googleapis.com/css2?family=Oswald:wght@500&family=Lato:wght@900&display=swap">
<style>
  :root {
    --page-bg: #d6d6d8;
    --navy-deep: #18246a;
    --navy: #1d3a8f;
    --royal: #1d5aab;
    --ink-black: #1b1b1b;
    --white: #ffffff;
  }
  * { margin: 0; padding: 0; box-sizing: border-box; }
  html, body { width: 879px; height: 1200px; overflow: hidden; }
  body { background: var(--page-bg); position: relative; }

  .banner {
    position: absolute;
    left: 40px; top: 433px;
    width: 800px; height: 334px;
    overflow: hidden;
    background: radial-gradient(ellipse 60% 70% at 55% 55%, var(--royal) 0%, var(--navy) 60%, var(--navy-deep) 100%);
  }
  .banner-shapes { position: absolute; inset: 0; }

  .brand-name {
    position: absolute;
    left: 40px; top: 70px;
    width: 290px;
    font-family: "Lato", sans-serif;
    font-weight: 900;
    font-size: 40px;
    line-height: 1.15;
    color: var(--white);
    text-align: center;
  }

  .headline {
    position: absolute;
    left: 366px; top: 38px;
    font-family: "Lato", sans-serif;
    font-weight: 900;
    text-transform: uppercase;
    color: var(--white);
    line-height: 1;
    letter-spacing: 2px;
  }
  .headline-line { display: block; font-size: 36px; }
  .headline-line + .headline-line { margin-top: 8px; }

  .tagline {
    position: absolute;
    left: 366px; top: 134px;
    font-family: "Lato", sans-serif;
    font-weight: 900;
    text-transform: uppercase;
    font-size: 25px;
    letter-spacing: 3px;
    color: var(--navy);
    line-height: 1;
  }

  .services {
    position: absolute;
    left: 353px; top: 181px;
    width: 390px; height: 52px;
    display: flex; align-items: center; justify-content: space-between;
    font-family: "Oswald", sans-serif;
    font-weight: 500;
    font-size: 25px;
    color: var(--white);
    list-style: none;
  }
  .services .divider { width: 2px; height: 26px; background: var(--white); }

  .contact {
    position: absolute;
    left: 36px; top: 268px;
    width: 742px;
    display: flex; align-items: center; justify-content: space-between;
    font-family: "Lato", sans-serif;
    font-weight: 900;
    font-size: 42px;
    color: var(--white);
    line-height: 1;
  }
  .contact-item { display: flex; align-items: center; gap: 12px; }
  .contact-icon { width: 36px; height: 36px; flex: none; }
</style>
</head>
<body>
  <section class="banner" aria-label="LRW Automotive outfield banner">
    <svg class="banner-shapes" viewBox="0 0 800 334" aria-hidden="true">
      <rect x="0" y="181" width="800" height="52" fill="var(--ink-black)"/>
      <rect x="340" y="126" width="438" height="40" fill="var(--white)"/>
    </svg>

    <div class="brand-name">LRW<br>Automotive</div>

    <h1 class="headline">
      <span class="headline-line">Total</span>
      <span class="headline-line">Vehicle Care</span>
    </h1>
    <p class="tagline">Company</p>

    <ul class="services">
      <li>TIRES</li><li class="divider"></li>
      <li>SERVICE</li><li class="divider"></li>
      <li>REPAIR</li><li class="divider"></li>
      <li>DIESEL</li>
    </ul>

    <div class="contact">
      <div class="contact-item location">
        <svg class="contact-icon" viewBox="0 0 36 36" aria-hidden="true">
          <path d="M18 3c-7 0-12 5-12 11.5C6 23 18 33 18 33s12-10 12-18.5C30 8 25 3 18 3z" fill="var(--white)"/>
          <circle cx="18" cy="14.5" r="5" fill="var(--navy)"/>
        </svg>
        <span>Maple Ridge</span>
      </div>
      <div class="contact-item phone">
        <svg class="contact-icon" viewBox="0 0 36 36" aria-hidden="true">
          <circle cx="18" cy="18" r="17" fill="var(--white)"/>
          <path d="M11 9.5c1-1 2.2-1 3 0l2 3c.6.9.4 1.8-.4 2.5l-1 .9c.9 2 2.6 3.8 4.6 4.7l.9-1c.7-.8 1.7-1 2.5-.4l3 2c1 .8 1 2 0 3l-1.4 1.3c-1.4 1.3-4 1-7.2-1.2-3.4-2.4-6-5.6-7.1-8.6-.8-2.2-.6-4 .7-5.1z" fill="var(--navy)"/>
          <path d="M20 9.5a7 7 0 0 1 6.5 6.5M20 13a3.5 3.5 0 0 1 3 3" stroke="var(--navy)" stroke-width="1.8" fill="none" stroke-linecap="round"/>
        </svg>
        <span>(555)214-3086</span>
      </div>
    </div>
  </section>
</body>
</html>
```